The BVR Relational Philanthropy Cycle

The title for this graphic is above. It must be included.
I am looking for a graphic representation of the relationship between the Christian school and the donor / pointing to the child (student) - the school's mission / outcome of investment through a gift / appreciation of the gift / communication of the gift impact for the child / stronger relationship going back to the child. This is not easy to do. I've tried to do it on my own and can't get it.
Any cliched child representations will be dismissed out of hand e.g. mortar boards, pencils, uniforms etc. The child should be abstract so that gender and race are irrelevant.
The key to this whole thing is the idea of RELATIONSHIP. The close relationship of donor and the Christian school, the pointing of that relationship to focus on the child / the school's mission, the outpouring of generosity that then happens in the heart of the donor and the gift that results, followed up by intentional work by the Christian school to thank and inform the donor - thank for the gift inform about the gift's expenditure and impact in the life of the child - all of which leads to a strengthening of the relationship and continued philanthropy as a never ending cycle.
It must be branded - logo and colors attached.
It must be obvious - easy to grasp the basic idea of relationship resulting in generosity / philanthropy. The visual should be clear - any words used illustrate - I should not 'need' the words to understand the idea.
I need it on a PP slide, jpeg, thumbnail. It must be highly legible in no more than 1/3 of a regular size piece of paper.
Our website is brightharborlearning.org
google donor cultivation cycle or donor giving cycle to see many examples of cycles that are used in secular contexts - the big difference in BVR's is the focus on the child and the importance of the relationship.

```html
<!DOCTYPE html>
<html lang="en">
<head>
<meta charset="utf-8">
<title>BVR Relational Philanthropy Cycle</title>
<link rel="stylesheet" href="https://fonts.googleapis.com/css2?family=Cinzel:wght@500&amp;family=Cormorant+Garamond:wght@500;600&amp;display=swap">
<style>
  :root {
    --brand-blue: #4677ad;
    --ring-grey: #8e8e8e;
    --cycle-grey: #c6cdd7;
    --coin-grey: #7d7d7d;
    --dots-grey: #8a8a8a;
    --paper: #ffffff;
    --credit-ink: #6b6b6b;
  }
  html, body {
    margin: 0;
    padding: 0;
    width: 1200px;
    height: 1177px;
    overflow: hidden;
    background: var(--paper);
  }
  .cycle-graphic {
    display: block;
    width: 1200px;
    height: 1177px;
  }
  .ring-fill { fill: var(--brand-blue); }
  .ring-cap { fill: var(--ring-grey); }
  .ring-child { fill: var(--cycle-grey); }
  .ring-core { fill: var(--paper); }
  .cycle-arc {
    fill: none;
    stroke: var(--cycle-grey);
    stroke-width: 6;
    stroke-linecap: round;
  }
  .cycle-head { fill: var(--cycle-grey); }
  .gift-flow {
    fill: none;
    stroke: var(--dots-grey);
    stroke-width: 3.2;
    stroke-linecap: round;
    stroke-dasharray: 0 8;
  }
  .gift-flow-head { fill: var(--dots-grey); }
  .icon-blue { fill: var(--brand-blue); }
  .icon-coin { fill: var(--coin-grey); }
  .icon-ribbon {
    fill: none;
    stroke: var(--brand-blue);
    stroke-width: 4;
  }
  .figure-slot { fill: #5f8bbd; }
  .ring-label {
    font-family: "Cinzel", "Cormorant Garamond", serif;
    font-size: 13px;
    font-weight: 500;
    fill: var(--paper);
    text-anchor: middle;
    letter-spacing: 0.3px;
  }
  .school-name {
    font-family: "Cinzel", serif;
    font-size: 31px;
    font-weight: 500;
    fill: var(--brand-blue);
    text-anchor: middle;
  }
  .coin-mark {
    font-family: "Cormorant Garamond", serif;
    font-size: 19px;
    font-weight: 600;
    fill: var(--paper);
    text-anchor: middle;
  }
  .icon-credit {
    font-family: "Cormorant Garamond", serif;
    font-size: 7.5px;
    fill: var(--credit-ink);
    text-anchor: middle;
  }
</style>
</head>
<body>
<svg class="cycle-graphic" viewBox="0 10 1000 981" xmlns="http://www.w3.org/2000/svg" role="img" aria-label="BVR Relational Philanthropy Cycle: donor and Christian school united in relationship, focused on the child">

  <!-- returning cycle arcs -->
  <g class="cycle-top">
    <path class="cycle-arc" d="M404 272 Q517 200 632 288"/>
    <path class="cycle-head" d="M395 282 L405 259 L415 279 Z"/>
    <path class="cycle-head" d="M643 297 L620 291 L637 275 Z"/>
  </g>
  <g class="cycle-bottom">
    <path class="cycle-arc" d="M348 585 Q380 735 517 737 Q654 735 690 590"/>
    <path class="cycle-head" d="M345 573 L335 596 L358 594 Z"/>
    <path class="cycle-head" d="M692 578 L680 600 L703 599 Z"/>
  </g>

  <!-- donor ring -->
  <g class="ring ring-donor">
    <circle class="ring-fill" cx="385" cy="433" r="122"/>
    <path class="ring-cap" d="M385 433 L298.7 346.7 A122 122 0 0 1 471.3 346.7 Z"/>
    <circle class="ring-core" cx="385" cy="433" r="62"/>
    <rect class="figure-slot" x="361" y="398" width="48" height="70" rx="10" role="img" aria-label="Donor figure icon with a heart on the chest"/>
    <text class="ring-label" x="385" y="351">DONOR</text>
  </g>

  <!-- school ring -->
  <g class="ring ring-school">
    <circle class="ring-fill" cx="645" cy="433" r="122"/>
    <path class="ring-cap" d="M645 433 L558.7 346.7 A122 122 0 0 1 731.3 346.7 Z"/>
    <circle class="ring-core" cx="645" cy="433" r="62"/>
    <text class="school-name" x="648" y="455">BVR</text>
    <text class="ring-label" x="645" y="343">CHRISTIAN</text>
    <text class="ring-label" x="645" y="359">SCHOOL</text>
  </g>

  <!-- child ring -->
  <g class="ring ring-child-group">
    <circle class="ring-child" cx="517" cy="567" r="122"/>
    <path class="ring-fill" d="M517 567 L603.3 653.3 A122 122 0 0 1 430.7 653.3 Z"/>
    <path class="ring-core" d="M517 452 C528 482 578 505 578 567 A61 61 0 1 1 456 567 C456 505 506 482 517 452 Z"/>
    <rect class="figure-slot" x="478" y="537" width="80" height="74" rx="10" role="img" aria-label="Two abstract children holding hands"/>
    <text class="ring-label" x="517" y="662">CHILD</text>
  </g>

  <!-- giving hand and coin -->
  <g class="icon-giving">
    <circle class="icon-coin" cx="530" cy="188" r="15"/>
    <text class="coin-mark" x="530" y="195">$</text>
    <rect class="icon-blue" x="488" y="210" width="9" height="20" rx="1"/>
    <path class="icon-blue" d="M500 212 L518 212 Q524 212 524 217 L536 217 L546 209 Q551 206 552 211 L540 226 L500 226 Z"/>
  </g>

  <!-- gift box -->
  <g class="icon-gift">
    <path class="icon-ribbon" d="M517 275 C505 258 492 264 499 273 Z M517 275 C529 258 542 264 535 273 Z"/>
    <rect class="icon-blue" x="481" y="277" width="72" height="18"/>
    <rect class="icon-blue" x="486" y="298" width="28" height="36"/>
    <rect class="icon-blue" x="520" y="298" width="28" height="36"/>
  </g>

  <!-- gift flow to child -->
  <path class="gift-flow" d="M517 344 L517 496"/>
  <path class="gift-flow-head" d="M502 503 L532 503 L517 530 Z"/>

  <!-- hearts of appreciation -->
  <g class="hearts icon-blue">
    <path d="M430 692 C418 684 416 676 421 672 C425 669 429 671 430 674 C431 671 435 669 439 672 C444 676 442 684 430 692 Z"/>
    <path d="M465 714 C453 706 451 698 456 694 C460 691 464 693 465 696 C466 693 470 691 474 694 C479 698 477 706 465 714 Z"/>
    <path d="M517 728 C499 716 497 705 504 700 C510 696 515 699 517 703 C519 699 524 696 530 700 C537 705 535 716 517 728 Z"/>
    <path d="M568 714 C556 706 554 698 559 694 C563 691 567 693 568 696 C569 693 573 691 577 694 C582 698 580 706 568 714 Z"/>
    <path d="M603 692 C591 684 589 676 594 672 C598 669 602 671 603 674 C604 671 608 669 612 672 C617 676 615 684 603 692 Z"/>
  </g>

  <text class="icon-credit" x="517" y="760">Icons by Iconfold from Glyphhouse.com</text>
</svg>
</body>
</html>
```